Blog Header Design + 2 Buttons + Colortheme

Hello,
I am looking for a fresh and catchy design for this blog project.
It can have a simplistic touch but I am open to all ideas which fit to the concept.
Please have a look at the pictures I've uploaded.
The website is called
http://www.wtwhn-blog.net
it is a blog which presents weird or extraordinary products. The URL is short for the german phrase "Was Toll Wäre Hier Nun?" it means "How cool is that?". Where "Geil" has the meaning of "Cool".
So yea, that is basically the idea of what it should stand for.
What I need is:
- a colortheme for the website
- a logo or banner at the top of the homesite (see the picture of the text I uploaded, if you could write it in this kind of deign that would look nice I guess)
- buttons for the product elements of the homesite and on the productdetail pages ("Geil!" Button and Price Button/Sign)
- background design (can fit the design idea but shouldnt be too distracting)
- if it is needed by or serves the design, the menu can be changed as well, but it can also stay as it is
optional for a complete set is needed:
- a favicon that fits the theme
- a facebook cover and profile picture
If you have any further questions please let know and I will respond to you as soon as possible.
Again, I am open to ALL design ideas for the whole website concept and would be glad to find a long term deign partner for other projects as well. THANK YOU!

```html
<!DOCTYPE html>
<html lang="de">
<head>
<meta charset="utf-8">
<title>Was Toll Wäre Hier Nun?</title>
<link href="https://fonts.googleapis.com/css2?family=PT+Sans:wght@400;700&display=swap" rel="stylesheet">
<style>
:root{
  --page:#f3f3f3;
  --topbar:#f5f5f5;
  --header:#444444;
  --nav:#2b2b2b;
  --nav-active:#000000;
  --green:#5aa51f;
  --green-dark:#3f7f12;
  --green-text:#4a9a16;
  --orange:#ffb41c;
  --orange-dark:#f08c00;
  --text:#555555;
  --border:#c8c8c8;
  --white:#ffffff;
}
*{margin:0;padding:0;box-sizing:border-box}
html,body{width:1200px;height:1000px;overflow:hidden}
body{background:var(--page);font-family:"PT Sans",sans-serif;color:var(--text);position:relative}
.topbar{height:42px;background:var(--topbar);border-bottom:2px solid #e2e2e2;display:flex;justify-content:flex-end;align-items:center;gap:6px;padding-right:27px}
.social-dot{width:32px;height:32px;border-radius:50%;background:#7d7d7d}
.site-header{height:208px;background:var(--header);position:relative}
.site-name{position:absolute;left:24px;top:40px;color:var(--white);font-weight:700;font-size:64px;line-height:70px;letter-spacing:1px;text-transform:uppercase}
.main-nav{height:65px;background:var(--nav);display:flex;align-items:center;position:relative}
.main-nav a{color:#eee;text-decoration:none;font-size:14px;position:absolute;top:0;height:65px;line-height:70px}
.main-nav a.active{background:var(--nav-active);color:var(--green);font-weight:700;left:26px;width:95px;text-align:center}
.search{position:absolute;left:950px;top:8px;width:226px;height:49px;border:1px solid #555;border-radius:8px;background:#333;color:#888;font-size:13px;padding-left:17px;line-height:50px}
.search .divider{position:absolute;left:180px;top:17px;width:1px;height:20px;background:#666}
.search svg{position:absolute;left:194px;top:15px}
.toolbar{position:absolute;top:342px;right:26px;display:flex;gap:12px;align-items:center}
.cards{position:absolute;top:412px;left:23px;display:flex;gap:23px}
.card{width:368px;height:478px;background:var(--white);border:1px solid var(--border);border-radius:8px;overflow:hidden;position:relative}
.card-photo{height:282px;background:linear-gradient(135deg,#e3ece8 0%,#d8b6a0 35%,#3d9a6b 70%,#e5e9e6 100%)}
.card-title{text-align:center;color:var(--green-text);font-size:18px;margin-top:14px}
.card-text{font-size:12px;line-height:19px;margin:12px 16px 0;color:#666}
.more{position:absolute;right:17px;top:372px;font-size:11px;color:var(--green-text);text-decoration:underline}
.btn-geil{position:absolute;left:14px;top:418px;width:97px;height:44px;border-radius:7px;background:linear-gradient(var(--green),var(--green-dark));color:#fff;font-weight:700;font-size:16px;display:flex;align-items:center;padding-left:20px;gap:12px}
.btn-geil .arrow{width:18px;height:18px;border-radius:50%;background:rgba(255,255,255,.35);display:flex;align-items:center;justify-content:center}
.price{position:absolute;right:13px;top:417px;width:97px;height:44px;border-radius:7px;background:linear-gradient(var(--orange),var(--orange-dark));display:flex;align-items:center;font-weight:700;color:#fff;font-size:17px}
.price .cur{width:33px;text-align:center;color:#333;font-weight:400;font-size:18px;border-right:1px solid rgba(0,0,0,.2);line-height:44px}
.price .amount{flex:1;text-align:center}
</style>
</head>
<body>
<div class="topbar">
  <span class="social-dot"></span><span class="social-dot"></span><span class="social-dot"></span><span class="social-dot"></span>
</div>
<header class="site-header">
  <div class="site-name">Was Toll Wäre<br>Hier Nun?</div>
</header>
<nav class="main-nav">
  <a class="active" href="#">Home</a>
  <a href="#" style="left:169px">Technik</a>
  <a href="#" style="left:251px">Spiel &amp; Spaß</a>
  <a href="#" style="left:379px">Kleidung &amp; Accessoires</a>
  <a href="#" style="left:559px">Haus &amp; Büro</a>
  <a href="#" style="left:667px">Essen &amp; Trinken</a>
  <a href="#" style="left:813px">Sonstiges</a>
  <div class="search">SEARCH<span class="divider"></span>
    <svg width="20" height="20" viewBox="0 0 20 20"><circle cx="8" cy="8" r="6" fill="none" stroke="#aaa" stroke-width="2"/><path d="M12.5 12.5 18 18" stroke="#aaa" stroke-width="3"/></svg>
  </div>
</nav>
<div class="toolbar">
  <svg width="20" height="20" viewBox="0 0 20 20"><rect x="1.5" y="3" width="17" height="15" fill="none" stroke="#444" stroke-width="2"/><rect x="1.5" y="3" width="17" height="4" fill="#444"/><path d="M5 10h10M5 13h10M5 16h10" stroke="#444"/></svg>
  <svg width="24" height="20" viewBox="0 0 24 20"><path d="M12 19 2 9a5 5 0 0 1 10-5 5 5 0 0 1 10 5z" fill="#6cc043"/></svg>
  <svg width="20" height="22" viewBox="0 0 20 22"><path d="M17 4a8 8 0 1 0 0 14M2 9h11M2 13h11" fill="none" stroke="#333" stroke-width="2"/></svg>
  <svg width="26" height="18" viewBox="0 0 26 18"><path d="M2 14 13 4l11 10" fill="none" stroke="#333" stroke-width="4"/></svg>
  <svg width="26" height="18" viewBox="0 0 26 18"><path d="M2 4l11 10L24 4" fill="none" stroke="#333" stroke-width="4"/></svg>
</div>
<main class="cards">
  <article class="card">
    <div class="card-photo" role="img" aria-label="Produktfoto: Kind trinkt durch einen bunten Strohhalm-Bausatz"></div>
    <h2 class="card-title">Strohhalm Bausatz</h2>
    <p class="card-text">Die Trinkhalm-Pipeline: Bau dir deine eigenen Röhren-Kreationen! Hoch, runter, um die Ecke, bastel eine endlose Reihe...</p>
    <a class="more" href="#">more&gt;&gt;</a>
    <div class="btn-geil">GEIL<span class="arrow"><svg width="8" height="10" viewBox="0 0 8 10"><path d="M2 1l4 4-4 4" fill="none" stroke="#fff" stroke-width="2"/></svg></span></div>
    <div class="price"><span class="cur">€</span><span class="amount">29,00</span></div>
  </article>
  <article class="card">
    <div class="card-photo" role="img" aria-label="Produktfoto: Kind trinkt durch einen bunten Strohhalm-Bausatz"></div>
    <h2 class="card-title">Strohhalm Bausatz</h2>
    <p class="card-text">Die Trinkhalm-Pipeline: Bau dir deine eigenen Röhren-Kreationen! Hoch, runter, um die Ecke, bastel eine endlose Reihe...</p>
    <a class="more" href="#">more&gt;&gt;</a>
    <div class="btn-geil">GEIL<span class="arrow"><svg width="8" height="10" viewBox="0 0 8 10"><path d="M2 1l4 4-4 4" fill="none" stroke="#fff" stroke-width="2"/></svg></span></div>
    <div class="price"><span class="cur">€</span><span class="amount">29,00</span></div>
  </article>
  <article class="card">
    <div class="card-photo" role="img" aria-label="Produktfoto: Kind trinkt durch einen bunten Strohhalm-Bausatz"></div>
    <h2 class="card-title">Strohhalm Bausatz</h2>
    <p class="card-text">Die Trinkhalm-Pipeline: Bau dir deine eigenen Röhren-Kreationen! Hoch, runter, um die Ecke, bastel eine endlose Reihe...</p>
    <a class="more" href="#">more&gt;&gt;</a>
    <div class="btn-geil">GEIL<span class="arrow"><svg width="8" height="10" viewBox="0 0 8 10"><path d="M2 1l4 4-4 4" fill="none" stroke="#fff" stroke-width="2"/></svg></span></div>
    <div class="price"><span class="cur">€</span><span class="amount">29,00</span></div>
  </article>
</main>
</body>
</html>
```